Brightway Haul & Repair Services, are a company that offers a 'one stop shop' pre-move clean up a

I have already selected a logo which I would like on the front of the business cards along with phone numbers, web address and email which are:
0419574302
www.brightwayhaul.com.au
brightwayhaulrepair@mailbox.example

On the back of the card I would like to list some of the types of service we offer (clean - move - repairs/maintenance) which are:
CLEAN - windows, gutters, solar panels, driveways/paths, carpets.
MOVE - Small/medium size house/office moves, large item pick-up & delivery, yard clean-up and removal.
General maintenance and repairs.

I would like the blue logo on a gray background.

Thanks

```html
<!DOCTYPE html>
<html lang="en">
<head>
<meta charset="utf-8">
<title>Brightway Haul &amp; Repair Services – Business Card</title>
<link href="https://fonts.googleapis.com/css2?family=Titillium+Web:ital,wght@0,400;0,600;0,700;1,700&display=swap" rel="stylesheet">
<style>
  :root {
    --stage: #3a3a3c;
    --card-white: #f4f5f6;
    --brand-blue: #1e8fd6;
    --deep-blue: #0f6fb8;
    --light-blue: #5cc0ec;
    --ink: #1d1d1f;
    --navy: #0b3760;
    --rule: #111111;
  }
  * { box-sizing: border-box; margin: 0; padding: 0; }
  html, body {
    width: 1200px; height: 900px; overflow: hidden;
    background: var(--stage);
    font-family: "Titillium Web", Arial, sans-serif;
  }
  .canvas {
    width: 1200px; height: 900px;
    display: flex; flex-direction: column;
    align-items: center; justify-content: center; gap: 56px;
  }
  .card {
    position: relative;
    width: 600px; height: 340px;
    overflow: hidden;
    box-shadow: 0 10px 30px rgba(0,0,0,.45);
  }

  /* Front */
  .card--front { background: var(--card-white); }
  .front-band { position: absolute; inset: 0; }
  .front-band .band-fill {
    position: absolute; left: 0; top: 0; width: 190px; height: 340px;
  }
  .brand {
    position: absolute; left: 236px; top: 44px;
  }
  .brand-name {
    font-weight: 700; font-size: 40px; line-height: 1;
    color: var(--brand-blue); text-transform: uppercase; letter-spacing: .5px;
    display: flex; align-items: center; gap: 10px;
  }
  .brand-mark {
    width: 14px; height: 14px; background: var(--brand-blue); display: inline-block;
  }
  .brand-tag {
    margin-top: 4px;
    font-weight: 600; font-size: 16px; letter-spacing: 1px;
    color: var(--ink); text-transform: uppercase;
  }
  .contact {
    position: absolute; left: 300px; top: 170px;
    list-style: none;
  }
  .contact li {
    display: flex; align-items: center; gap: 10px;
    font-size: 15px; color: var(--ink); height: 28px;
  }
  .contact li.email { font-size: 13px; }
  .contact-icon {
    width: 18px; height: 18px; background: var(--brand-blue);
    display: flex; align-items: center; justify-content: center; flex: none;
  }

  /* Back */
  .card--back {
    background: linear-gradient(160deg, var(--light-blue) 0%, var(--brand-blue) 45%, var(--deep-blue) 100%);
  }
  .back-brand {
    position: absolute; right: 34px; top: 30px;
    font-weight: 700; font-size: 24px; color: #ffffff;
    text-transform: uppercase; letter-spacing: .5px;
  }
  .services {
    position: absolute; left: 40px; top: 100px; right: 40px;
    list-style: none;
  }
  .services li {
    font-weight: 700; font-style: italic;
    font-size: 18px; line-height: 1.3; color: var(--navy);
    margin-bottom: 14px;
  }
  .services .service-head { text-transform: uppercase; }
</style>
</head>
<body>
<main class="canvas">

  <section class="card card--front" aria-label="Business card front">
    <svg class="front-band" width="600" height="340" viewBox="0 0 600 340">
      <defs>
        <linearGradient id="bandGrad" x1="0" y1="0" x2="1" y2="0">
          <stop offset="0" stop-color="#1577c2"/>
          <stop offset="1" stop-color="#5ab8e6"/>
        </linearGradient>
      </defs>
      <path d="M0 0 H70 Q230 170 70 340 H0 Z" fill="url(#bandGrad)" role="img" aria-label="Blue band with faint wrench motif"/>
      <path d="M70 0 Q230 170 70 340" fill="none" stroke="var(--rule)" stroke-width="5"/>
      <path d="M78 0 Q238 170 78 340" fill="none" stroke="#bfc3c7" stroke-width="2"/>
    </svg>

    <div class="brand">
      <div class="brand-name"><span class="brand-mark"></span>Brightway Haul</div>
      <div class="brand-tag">&amp; Repair Services</div>
    </div>

    <ul class="contact">
      <li>
        <span class="contact-icon">
          <svg width="12" height="12" viewBox="0 0 24 24"><path fill="#fff" d="M6.6 10.8a15 15 0 0 0 6.6 6.6l2.2-2.2c.3-.3.7-.4 1-.2 1.1.4 2.3.6 3.6.6.6 0 1 .4 1 1V20c0 .6-.4 1-1 1C10.6 21 3 13.4 3 4c0-.6.4-1 1-1h3.5c.6 0 1 .4 1 1 0 1.3.2 2.5.6 3.6.1.3 0 .7-.2 1z"/></svg>
        </span>0419574302
      </li>
      <li>
        <span class="contact-icon">
          <svg width="12" height="12" viewBox="0 0 24 24"><circle cx="12" cy="12" r="9" fill="none" stroke="#fff" stroke-width="2"/><path d="M3 12h18M12 3c3 3 3 15 0 18M12 3c-3 3-3 15 0 18" fill="none" stroke="#fff" stroke-width="1.6"/></svg>
        </span>www.brightwayhaul.com.au
      </li>
      <li class="email">
        <span class="contact-icon">
          <svg width="12" height="12" viewBox="0 0 24 24"><rect x="3" y="6" width="18" height="12" fill="none" stroke="#fff" stroke-width="2"/><path d="M3 6l9 7 9-7" fill="none" stroke="#fff" stroke-width="2"/></svg>
        </span>brightwayhaulrepair@mailbox.example
      </li>
    </ul>
  </section>

  <section class="card card--back" aria-label="Business card back">
    <div class="back-brand">Brightway Haul</div>
    <ul class="services">
      <li><span class="service-head">Clean</span> - windows, gutters, solar panels, driveways/paths-carpets</li>
      <li><span class="service-head">Move</span> - small/medium size house/office moves, large item pick-up &amp; delivery, yard clean-up and removal.</li>
      <li>General maintenance and repairs.</li>
    </ul>
  </section>

</main>
</body>
</html>
```